Landing page for Varnika Computer Support

We need a high converting landing page for PPC campaign for Varnika Computer Support. We are looking for a responsive page which works for PC, MAC and Mobile devices. Main purpose of page will be to generate calls to our Toll free number. Users can also opt for chat with technician to resolve their issues but only CTA of page should be to generate call to our toll free number.
Current landing page we use is- https://pelquorahelp.com/varnika-computer-support.html (called Link1 in text below)
We will need following in new landing page:
1. Disclaimer - This is legally mandatory near CTA
BrindleMend is an independent provider of technical support services for several third party brands. If your product is under warranty or not repair service maybe available at brand owner or official website. Use of names, trademarks is for reference only. We disclaim any ownership, right, affiliation or endorsement of or by any such third party products or brands.
2. New Image of Customer Service Rep. See Link1
3. Description/details of what support for Varnika we provide. See Link1. You can take some or all content from link1
4. Testimonials
5. Chat option
6. Footer with following- Contact Info and copyright statement. See Link1
7. You can place trust building logo like Holvast Guard and Selbyrook to your choice to increase effectiveness of landing page
Take ideas from http://quorvelpages.com/landing-page-articles/the-anatomy-of-a-landing-page/. We can put whatever is necessary on new landing page to reach goal of high conversions.
Landing pages designs we like:
http://www.setup-shieldware.com/5029174/dornick/dornick-support.html
http://www.mentorvix.com/varnika/varnika_support/varnika_help_support.php
http://breezbitly.com/fix-computer/
New Details:
-----------------
I generally prefer white background for landing pages. You can also use grey and any other color which goes with it. In the end, goal is high conversion rate.
Updates
Since some of the designs posted have ability to collect email address, I would like to clarify that Only CTA is to call toll free number. We don't need to collect email addresses. Reason is 99.9% of customers will only reach out to us if they have an urgent and immediate problem to resolve. They will call toll free and get support via remote connection but won't send email. Very few will opt to chat with technician. Even if they send email, they will never buy our services because they would have contacted somebody else to solve their immediate problem via remote connection.
Thanks
Home users and small business

```html
<!DOCTYPE html>
<html lang="en">
<head>
<meta charset="utf-8">
<title>PelquoraHelp – Varnika Computer Support</title>
<link rel="stylesheet" href="https://fonts.googleapis.com/css2?family=Arimo:wght@400;700&family=Roboto+Condensed:wght@400;700&family=Raleway:wght@300;400&family=Source+Sans+3:wght@400;700&family=Damion&display=swap">
<style>
:root{
  --ink:#2b2b2b;
  --muted:#555;
  --blue:#1e5f9e;
  --blue-light:#3a8ad2;
  --blue-deep:#1b5a98;
  --page:#f0f0ee;
  --white:#fff;
  --black:#111;
  --gold:#f3be16;
  --gold-dark:#e3a40a;
  --gold-ring:#1d4f86;
  --script-red:#d6262b;
  --panel-line:#cfcfcf;
  --band:#a9b4b4;
  --footer:#1c5c9b;
}
*{box-sizing:border-box;margin:0;padding:0}
html,body{width:705px;height:1200px;overflow:hidden}
body{position:relative;background:var(--page);font-family:Arimo,Arial,sans-serif;color:var(--ink)}
.abs{position:absolute}

.site-header{left:0;top:0;width:705px;height:61px;background:var(--white)}
.brand{display:flex;align-items:center;gap:5px;font-family:"Roboto Condensed",sans-serif;font-weight:400;color:#2a2a2a;white-space:nowrap}
.brand-dot{width:14px;height:14px;border-radius:50%;background:#8a8a8a}
.site-header .brand{left:70px;top:17px;font-size:21px}
.header-phone{left:498px;top:18px;display:flex;gap:6px;align-items:center;color:#777;white-space:nowrap}
.header-phone small{display:block;font-size:8px;line-height:9px}
.header-phone strong{display:block;font-size:15px;font-weight:400;line-height:16px}

.hero{left:0;top:61px;width:705px;height:285px;background:linear-gradient(180deg,#1f66ad 0%,var(--blue-light) 55%,#2f7fc7 65%,var(--blue-deep) 65.1%,var(--blue-deep) 100%)}
.video{left:82px;top:91px;width:283px;height:180px;background:#111;padding:3px;box-shadow:0 6px 14px rgba(0,0,0,.45)}
.video-still{width:100%;height:100%;background:linear-gradient(120deg,#6b5a4c,#d6b8a0 45%,#c7a58a 60%,#4e4136)}
.video-bar{left:88px;top:244px;width:271px;height:20px;background:rgba(0,0,0,.75);display:flex;align-items:center;padding:0 8px;gap:10px}
.video-track{flex:1;height:5px;background:#555}
.video-track span{display:block;width:88%;height:100%;background:#2a2a2a;border-right:10px solid #4aa2e0}

.hero-quote{left:84px;top:292px;width:284px;color:var(--white);font-size:8px;line-height:13px}
.hero-quote .mark{font-family:Georgia,serif;font-size:16px;vertical-align:-3px}
.hero-quote cite{display:block;text-align:right;font-style:italic;margin-top:4px}

.call-panel{left:434px;top:90px;width:211px;height:314px;background:var(--white);border:1px solid #ccc;border-radius:4px;overflow:hidden}
.call-panel h2{height:32px;background:var(--black);color:var(--white);font-size:17px;font-weight:700;text-align:center;line-height:34px}
.panel-body{padding:9px 14px 0}
.panel-intro{font-family:"Source Sans 3",sans-serif;font-size:8.2px;line-height:13px;color:#333}
.toll-label{margin-top:12px;font-size:7.5px;color:#333}
.toll-number{margin-top:4px;display:flex;align-items:center;gap:6px;font-size:19px;font-weight:700;color:var(--blue);white-space:nowrap}
.cta{display:block;margin-top:12px;height:34px;border-radius:3px;background:linear-gradient(var(--gold),var(--gold-dark));border:1px solid #c99000;font-size:19px;text-align:center;line-height:33px;color:#1a1a1a}
.cta-note{font-size:7.4px;color:#444;margin-top:8px}
.disclaimer{margin-top:8px;padding-top:7px;border-top:1px solid #e2e2e2;font-size:6.3px;line-height:8.6px;color:#666}

.intro{left:60px;top:364px;width:348px;font-size:7.6px;line-height:13px;color:#333}

.feature{left:58px;display:flex;align-items:center;gap:11px;font-family:"Roboto Condensed",sans-serif;font-size:11.5px;color:#222;white-space:nowrap}
.feature-num{width:35px;height:35px;border-radius:50%;background:var(--gold);border:2px solid var(--gold-ring);display:flex;align-items:center;justify-content:center;font-family:Arimo,sans-serif;font-size:14px;color:#111}

.testimonial{left:434px;top:424px;width:212px;height:151px;background:var(--white);border:1px solid #ccc;border-radius:8px;padding:10px 12px}
.testimonial h3{font-family:Damion,cursive;font-weight:400;color:var(--script-red);font-size:15px;line-height:15px;border-bottom:1px solid #ddd;padding-bottom:10px;margin-bottom:10px}
.testimonial p{font-size:7.3px;line-height:12.8px;color:#333}
.author{left:502px;top:589px;font-size:7px;line-height:14px;color:#444}
.author b{font-weight:700}
.avatar{left:597px;top:589px;width:22px;height:22px;border-radius:50%;background:linear-gradient(#c9c9c9,#8a8f96);border:2px solid #fff;box-shadow:0 0 0 1px #ccc}

.reinforce{left:0;top:650px;width:705px;height:58px;background:var(--white);display:flex;align-items:center;justify-content:center;font-family:Raleway,sans-serif;font-weight:400;font-size:24px;color:var(--blue)}

.card{width:152px}
.card .photo{height:69px;border:5px solid #d6d6d6}
.card p{margin-top:10px;font-size:7.1px;line-height:10.6px;color:#444}
.team{background:linear-gradient(90deg,#e8eef2,#4a3d35 30%,#e0e6ea 50%,#3a3f48 80%,#dfe6ea)}
.deal{background:linear-gradient(90deg,#4a4d52,#bfc3c7 40%,#e7e8e9 60%,#9ea3a8)}
.reps{background:linear-gradient(90deg,#f0f0f0,#3d3631 25%,#efefef 45%,#4c4036 70%,#eeeeee)}

.call-band{left:66px;top:1044px;width:570px;height:57px;background:var(--band);border-radius:3px;z-index:2}
.band-title{left:30px;top:16px;font-family:Raleway,sans-serif;color:#333;line-height:12px;white-space:nowrap}
.band-title b{display:block;font-weight:400;font-size:14px}
.band-title span{font-size:9.5px;letter-spacing:1.5px}
.band-number{left:228px;top:19px;display:flex;align-items:center;gap:6px;font-size:16px;font-weight:700;color:#1d3f63;white-space:nowrap}
.band-chat{left:380px;top:23px;font-size:8px;color:#333;white-space:nowrap}
.band-btn{left:478px;top:16px;width:70px;height:23px;background:var(--black);color:var(--white);font-size:8.5px;text-align:center;line-height:23px;border-radius:2px}

.site-footer{left:0;top:1078px;width:705px;height:122px;background:var(--footer);color:var(--white);font-size:7.3px;line-height:9px}
.foot-col{top:39px}
.foot-col h4{font-size:7.5px;font-weight:700;margin-bottom:11px}
.foot-col p + p{margin-top:12px}
.social{display:flex;gap:6px;margin-bottom:9px}
.social i{width:16px;height:16px;border-radius:50%;background:#f3f3f3}
.site-footer .brand{left:504px;top:52px;font-size:20px;color:var(--white)}
.site-footer .brand-dot{background:#d0d8e2}
</style>
</head>
<body>

<header class="abs site-header">
  <div class="abs brand"><span class="brand-dot"></span>PelquoraHelp</div>
  <div class="abs header-phone">
    <svg width="18" height="18" viewBox="0 0 24 24"><path fill="#8a8a8a" d="M6.6 10.8c1.4 2.8 3.8 5.1 6.6 6.6l2.2-2.2c.3-.3.7-.4 1-.2 1.1.4 2.3.6 3.6.6.6 0 1 .4 1 1V20c0 .6-.4 1-1 1C10.6 21 3 13.4 3 4c0-.6.4-1 1-1h3.5c.6 0 1 .4 1 1 0 1.3.2 2.5.6 3.6.1.3 0 .7-.2 1z"/></svg>
    <div><small>Call Now Today</small><strong>+1 (800) 555-0142</strong></div>
  </div>
</header>

<section class="abs hero"></section>

<div class="abs video"><div class="video-still" role="img" aria-label="Video still of smiling support agents wearing headsets"></div></div>
<div class="abs video-bar">
  <svg width="10" height="10" viewBox="0 0 10 10"><path d="M1 0l9 5-9 5z" fill="#fff"/></svg>
  <div class="video-track"><span></span></div>
</div>

<blockquote class="abs hero-quote">
  <span class="mark">&ldquo;</span> we thought doing business in the region would be a piece of cake, 2 years later, after wasting hundreds of thousands of dollars... <span class="mark">&rdquo;</span>
  <cite>Marla Denton Oake</cite>
</blockquote>

<aside class="abs call-panel">
  <h2>Talk to a Technician</h2>
  <div class="panel-body">
    <p class="panel-intro">Having trouble with your Varnika computer? Call our certified technicians now and get it fixed fast through a secure remote connection.</p>
    <p class="toll-label">Toll Free, 24/7 Support</p>
    <div class="toll-number">
      <svg width="16" height="16" viewBox="0 0 24 24"><path fill="#1e5f9e" d="M6.6 10.8c1.4 2.8 3.8 5.1 6.6 6.6l2.2-2.2c.3-.3.7-.4 1-.2 1.1.4 2.3.6 3.6.6.6 0 1 .4 1 1V20c0 .6-.4 1-1 1C10.6 21 3 13.4 3 4c0-.6.4-1 1-1h3.5c.6 0 1 .4 1 1 0 1.3.2 2.5.6 3.6.1.3 0 .7-.2 1z"/></svg>
      +1 (800) 555-0142
    </div>
    <span class="cta">Call to Action</span>
    <p class="cta-note">Prefer to type? Chat with a technician.</p>
    <p class="disclaimer">BrindleMend is an independent provider of technical support services for several third party brands. If your product is under warranty or not repair service maybe available at brand owner or official website. Use of names, trademarks is for reference only. We disclaim any ownership, right, affiliation or endorsement of or by any such third party products or brands.</p>
  </div>
</aside>

<p class="abs intro">When you face a computer problem, identifying the problem and properly fixing it consumes precious time, labor, and resources. We are here to streamline the tech support process, offering high-quality, professional tech support for Varnika computers. All of our technicians are fully certified and trained, with experience and expertise dealing specifically with Varnika computers. Our technicians can efficiently deal with a range of problems and issues, including:</p>

<div class="abs feature" style="top:447px"><span class="feature-num">1</span>Your first feature written in the form of a benifit statement</div>
<div class="abs feature" style="top:503px;gap:7px"><span class="feature-num">2</span>Your Second feature written in the form of a benifit statement</div>
<div class="abs feature" style="top:564px;gap:7px"><span class="feature-num">3</span>Your Third feature written in the form of a benifit statement</div>

<aside class="abs testimonial">
  <h3>The results are based on<br>client's reality</h3>
  <p>&ldquo;Initially, we thought doing business in the region would be a piece of cake, 2 years later, after wasting hundreds of thousands of dollars, we realized how wrong we were. Ones we were introduced to Quillon's team, reaching decision makers and key customers was only a matter of a phone call away.&rdquo;</p>
</aside>
<svg class="abs" style="left:612px;top:573px" width="18" height="12"><path d="M0 0h18L8 12z" fill="#fff" stroke="#ccc"/><path d="M1 0h16" stroke="#fff" stroke-width="2"/></svg>
<div class="abs author">Corwin J. Tallis - USA<br><b>Fenmarsh Systems</b></div>
<div class="abs avatar" role="img" aria-label="Customer portrait"></div>

<h2 class="abs reinforce">A reinforcement statement to maintain interest</h2>

<div class="abs card" style="left:72px;top:753px"><div class="photo team" role="img" aria-label="Photo of a business team looking up"></div><p>Vestibulum rutrum pharetra diam, eget dapibus leo vehicula ut. Fusce aliquam, odio eget adipiscing lobortis, nisl sapien placerat est...</p></div>
<div class="abs card" style="left:271px;top:753px"><div class="photo deal" role="img" aria-label="Photo of a business handshake"></div><p>Vestibulum rutrum pharetra diam, eget dapibus leo vehicula ut. Fusce aliquam, odio eget adipiscing lobortis, nisl sapien placerat est...</p></div>
<div class="abs card" style="left:470px;top:753px"><div class="photo reps" role="img" aria-label="Photo of support reps with headsets"></div><p>Vestibulum rutrum pharetra diam, eget dapibus leo vehicula ut. Fusce aliquam, odio eget adipiscing lobortis, nisl sapien placerat est...</p></div>
<div class="abs card" style="left:71px;top:900px"><div class="photo team" role="img" aria-label="Photo of a business team looking up"></div><p>Vestibulum rutrum pharetra diam, eget dapibus leo vehicula ut. Fusce aliquam, odio eget adipiscing lobortis, nisl sapien placerat est...</p></div>
<div class="abs card" style="left:270px;top:900px"><div class="photo deal" role="img" aria-label="Photo of a business handshake"></div><p>Vestibulum rutrum pharetra diam, eget dapibus leo vehicula ut. Fusce aliquam, odio eget adipiscing lobortis, nisl sapien placerat est...</p></div>
<div class="abs card" style="left:469px;top:900px"><div class="photo reps" role="img" aria-label="Photo of support reps with headsets"></div><p>Vestibulum rutrum pharetra diam, eget dapibus leo vehicula ut. Fusce aliquam, odio eget adipiscing lobortis, nisl sapien placerat est...</p></div>

<footer class="abs site-footer">
  <div class="abs foot-col" style="left:73px">
    <h4>EUROPE</h4>
    <p>12 Harlow Row<br>Dunmere, DM4 2QT</p>
    <p>Phone:+44(0)1632 960417<br>Email:eu@ruvellodata.com</p>
  </div>
  <div class="abs foot-col" style="left:194px">
    <h4>NORTH AMERICA</h4>
    <p>4100 Lakeline Ave, Suite 210<br>Corvale, TX 75099</p>
    <p>Phone:(555) 019 4472<br>Email:us@ruvellodata.com</p>
  </div>
  <div class="abs foot-col" style="left:329px">
    <h4>FOLLOW US ONLINE</h4>
    <div class="social"><i></i><i></i><i></i><i></i></div>
    <p>Privacy Policy | Terms of Services | Sitemap<br><span style="display:block;margin-top:3px">Copyright © 2014. All Rights Reserved.</span></p>
  </div>
  <div class="abs brand"><span class="brand-dot"></span>PelquoraHelp</div>
</footer>

<div class="abs call-band">
  <div class="abs band-title"><b>NEED HELP NOW?</b><span>CALL TOLL FREE</span></div>
  <div class="abs band-number">
    <svg width="14" height="14" viewBox="0 0 24 24"><path fill="#1d3f63" d="M6.6 10.8c1.4 2.8 3.8 5.1 6.6 6.6l2.2-2.2c.3-.3.7-.4 1-.2 1.1.4 2.3.6 3.6.6.6 0 1 .4 1 1V20c0 .6-.4 1-1 1C10.6 21 3 13.4 3 4c0-.6.4-1 1-1h3.5c.6 0 1 .4 1 1 0 1.3.2 2.5.6 3.6.1.3 0 .7-.2 1z"/></svg>
    +1 (800) 555-0142
  </div>
  <div class="abs band-chat">or chat with us</div>
  <div class="abs band-btn">Call Now</div>
</div>

</body>
</html>
```